Locksmith SmartPhone Web Design Project

I am a locksmith and focus on customers that use their smart phones to find me. I have a static web page that I created myself but it is horrible. See for yourself at www.brevalkeyworks.com.au

I want a cross-platform static site that simply shows the information and with the ability to change minor items like pricing. I want it to be compelling in its look and feel (not overwhelming) but simple. It must have a; click to call button; the ability to install a hit counter from pagetallyo.com; payment information just like the current graphic of card/cash/quidlo (orla/brixalonte only).

This will be hosted on my own server.
Updates

Hello Designers,

I have updated the brief in the must have and nice to have fields.

Thank you all,

Tom.

Hello to all Designers,

There is about 9 days left before the deadline. The overall level of competition is extremely high and I would like to thank all the designers who have submitted so far, 27 submissions in total so far. Excellent work.

If you have submitted already and wish to provide new designs, I am keen to see them. 

Hi guys, time is almost up. Please submit any new designs that you may have. The quality has been excellent so far.

Tom.

Target Market(s)

People who are locked out of their house/shop/office etc.

Industry/Entity Type

Locksmith

Requirements
Must have
• click to call button
hit counter from pagetallyo
payment graphic card/cash/quidlo (orla/brixalonte only)
cross platform compatibility smartphone/phablet
Single column page preferable, can have two columns.
Nice to have
• When the page loads regardless of the mobile device, all info should be presented. In other words no vertical or horizontal scroll bars.
Should not have
• hidden code, advertising, credits etc

```html
<!DOCTYPE html>
<html lang="en">
<head>
<meta charset="utf-8">
<title>Breval Keyworks – Locksmith Lockout Service</title>
<link href="https://fonts.googleapis.com/css2?family=Lato:wght@300;400;700&display=swap" rel="stylesheet">
<style>
  :root {
    --header-top: #4aa3e0;
    --header-bottom: #2a82c6;
    --page-bg: #ececec;
    --footer-bg: #ffffff;
    --text-main: #555555;
    --text-soft: #9a9a9a;
    --brand-blue: #1f74d6;
    --brand-red: #ea3a26;
    --brand-dark: #111111;
    --go-green-top: #9bd84a;
    --go-green-bottom: #5ea81c;
    --lock-orange: #f5a21b;
    --lock-shackle: #b9b9b9;
    --key-gold: #e7b21f;
    --cash-green: #8fae7a;
    --card-border: #cfcfcf;
    --white: #ffffff;
  }
  * { margin: 0; padding: 0; box-sizing: border-box; }
  html, body { width: 756px; height: 1200px; overflow: hidden; }
  body {
    position: relative;
    background: var(--page-bg);
    font-family: "Lato", sans-serif;
    color: var(--text-main);
  }
  .site-header {
    position: absolute; left: 0; top: 0; width: 756px; height: 113px;
    background: linear-gradient(var(--header-top), var(--header-bottom));
    color: var(--white);
    display: flex; align-items: center; justify-content: center;
  }
  .site-title { font-weight: 400; font-size: 58px; letter-spacing: 0.5px; }
  .site-title sup { font-size: 22px; vertical-align: 28px; margin-left: 2px; }

  .padlock-art {
    position: absolute; left: 56px; top: 198px; width: 120px; height: 166px;
    border-radius: 20px;
    background: linear-gradient(var(--lock-shackle) 0 34%, var(--lock-orange) 34% 100%);
  }
  .lockout-heading {
    position: absolute; left: 230px; top: 194px; width: 420px; text-align: center;
  }
  .lockout-heading h1 { font-weight: 400; font-size: 64px; line-height: 1.1; color: var(--text-main); }
  .lockout-heading p { font-size: 34px; margin-top: 8px; color: var(--text-main); }

  .service-line {
    position: absolute; left: 0; top: 398px; width: 756px; text-align: center;
    font-size: 46px; font-weight: 400;
  }
  .service-line .word-blue { color: var(--brand-blue); }
  .service-line .word-red { color: var(--brand-red); }
  .service-line .word-dark { color: var(--brand-dark); }
  .key-art {
    position: absolute; left: 634px; top: 450px; width: 58px; height: 78px;
    border-radius: 28px 28px 12px 12px;
    background: linear-gradient(160deg, #f4cf55, var(--key-gold));
  }

  .clock-line {
    position: absolute; left: 0; top: 545px; width: 756px; text-align: center;
    font-size: 27px; font-weight: 300; color: var(--text-soft);
  }
  .availability {
    position: absolute; left: 0; top: 628px; width: 756px;
    display: flex; align-items: center; justify-content: center; gap: 22px;
  }
  .availability-label { font-size: 42px; font-weight: 400; color: var(--text-main); }
  .availability-badge {
    width: 72px; height: 66px; border-radius: 50%;
    background: radial-gradient(circle at 40% 35%, #b6e25a, #7dbb23);
    color: var(--white); font-weight: 700; font-size: 28px;
    display: flex; align-items: center; justify-content: center;
  }

  .call-button {
    position: absolute; left: 110px; top: 717px; width: 540px; height: 112px;
    border-radius: 56px;
    background: linear-gradient(var(--go-green-top), var(--go-green-bottom));
    box-shadow: inset 0 3px 0 rgba(255,255,255,0.35), 0 3px 5px rgba(0,0,0,0.2);
    color: var(--white); text-decoration: none;
    display: flex; align-items: center;
  }
  .call-icon { width: 96px; height: 96px; margin-left: 12px; }
  .call-label { flex: 1; text-align: center; font-size: 54px; font-weight: 400; padding-right: 60px; }

  .payment-methods {
    position: absolute; left: 110px; top: 858px; width: 540px; height: 94px;
    display: flex; align-items: center; gap: 8px;
  }
  .pay-card {
    height: 86px; border: 2px solid var(--card-border); border-radius: 6px;
    background: var(--white);
    display: flex; align-items: center; justify-content: center;
    font-size: 22px; font-weight: 700; color: var(--text-main);
  }
  .pay-card.orla { width: 150px; }
  .pay-card.brixalonte { width: 158px; }
  .pay-card.quidlo { width: 118px; }
  .cash-art {
    width: 90px; height: 86px; border-radius: 6px;
    background: linear-gradient(135deg, #b8cca6, var(--cash-green));
  }

  .business-ids {
    position: absolute; left: 0; top: 988px; width: 756px; text-align: center;
    font-size: 29px; font-weight: 300; color: var(--text-soft); line-height: 54px;
  }
  .site-footer {
    position: absolute; left: 0; top: 1120px; width: 756px; height: 80px;
    background: var(--footer-bg);
    display: flex; align-items: center; justify-content: center;
  }
  .hit-counter { font-size: 25px; color: var(--text-main); }
</style>
</head>
<body>
  <header class="site-header">
    <div class="site-title">Breval Keyworks<sup>®</sup></div>
  </header>

  <div class="padlock-art" role="img" aria-label="Orange padlock with keyhole"></div>
  <div class="lockout-heading">
    <h1>Locked Out?</h1>
    <p>$150 Gets You In. EASY!</p>
  </div>

  <div class="service-line">
    <span class="word-blue">Locksmith</span>
    <span class="word-red">Lockout</span>
    <span class="word-dark">Service</span>
  </div>
  <div class="key-art" role="img" aria-label="Gold key hanging from the service title"></div>

  <div class="clock-line">It is now 11:29:42 AM</div>

  <div class="availability">
    <span class="availability-label">Locksmith Available?</span>
    <span class="availability-badge">yes</span>
  </div>

  <a class="call-button" href="tel:0000000000">
    <svg class="call-icon" viewBox="0 0 96 96" aria-hidden="true">
      <circle cx="48" cy="48" r="44" fill="#6fb52a" stroke="#ffffff" stroke-width="5"/>
      <path d="M34 26c3-2 6-1 7 2l4 9c1 2 0 4-2 5l-4 3c2 6 7 11 13 14l3-4c1-2 3-3 5-2l9 4c3 1 4 4 2 7l-3 5c-2 3-6 4-10 3-16-5-28-17-33-33-1-4 0-8 3-10z" fill="#ffffff"/>
    </svg>
    <span class="call-label">Click to Call</span>
  </a>

  <div class="payment-methods">
    <div class="pay-card orla">orla</div>
    <div class="pay-card brixalonte">brixalonte</div>
    <div class="cash-art" role="img" aria-label="Fanned banknotes for cash payment"></div>
    <div class="pay-card quidlo">quidlo</div>
  </div>

  <div class="business-ids">
    <div>ABN: 61207384951</div>
    <div>Master Licence: 392160847</div>
  </div>

  <footer class="site-footer">
    <span class="hit-counter">1,971</span>
  </footer>
</body>
</html>
```